MEDICAL CLINIC LETTERHEAD

Design is a letterhead for a non-profit medical center. The name of the clinic is VYRLOTEN Community Health Center. Although the full name must be included, the community health center part is more of a description and should be less visible - i attached an example of what I mean by that (ATTACHED IMAGE IS AN EXAMPLE OF FONT SIZES NOT A DESIGN IDEA). Please design something modern, cool looking and unique because I can always download free templates.
Phone, email, website and etc will be added later.

Industry/Entity Type

MEDICAL

```html
<!DOCTYPE html>
<html lang="en">
<head>
<meta charset="utf-8">
<title>VYRLOTEN Community Health Center – Letterhead</title>
<link href="https://fonts.googleapis.com/css2?family=Open+Sans:wght@400;700&family=Roboto:ital,wght@1,400&display=swap" rel="stylesheet">
<style>
  :root {
    --navy: #13487a;
    --green: #5a9a3c;
    --ink: #555a60;
    --paper: #ffffff;
    --backdrop: #e6e7e9;
  }
  html, body {
    margin: 0;
    width: 1200px;
    height: 1048px;
    overflow: hidden;
    background: var(--backdrop);
  }
  .letterhead {
    position: absolute;
    left: 253px;
    top: 34px;
    width: 694px;
    height: 980px;
    background: var(--paper);
    box-shadow: 0 6px 24px rgba(0,0,0,0.18);
    font-family: "Open Sans", sans-serif;
    color: var(--ink);
    overflow: hidden;
  }
  .brand {
    position: absolute;
    left: 60px;
    top: 58px;
  }
  .brand-name {
    display: flex;
    align-items: center;
    gap: 8px;
    font-weight: 700;
    font-size: 28px;
    letter-spacing: 0.5px;
    color: var(--navy);
    line-height: 1;
  }
  .brand-dot {
    width: 12px;
    height: 12px;
    border-radius: 50%;
    background: var(--navy);
  }
  .brand-tagline {
    margin-top: 5px;
    font-size: 11px;
    letter-spacing: 0.4px;
    text-transform: uppercase;
    color: var(--green);
  }
  .contact {
    position: absolute;
    right: 60px;
    top: 62px;
    font-family: "Roboto", sans-serif;
    font-style: italic;
    font-size: 11.5px;
    line-height: 1.35;
    color: #333;
  }
  .contact-address { margin: 0 0 8px; text-align: right; }
  .contact-list { list-style: none; margin: 0; padding: 0; }
  .contact-list li { display: flex; align-items: center; gap: 6px; }
  .contact-list svg { width: 10px; height: 10px; fill: var(--green); flex: none; }
  .letter {
    position: absolute;
    left: 60px;
    right: 60px;
    top: 190px;
    font-size: 11.5px;
    line-height: 1.55;
  }
  .letter p { margin: 0 0 14px; text-align: justify; }
  .letter .salutation { margin-bottom: 16px; }
  .signature {
    width: 80px;
    height: 54px;
    margin-top: 18px;
    background: linear-gradient(135deg, #eef1f5, #dfe5ee);
  }
  .footer-band {
    position: absolute;
    left: 0;
    bottom: 0;
    width: 100%;
    height: 12px;
    display: flex;
  }
  .footer-band .accent { width: 72px; background: var(--green); }
  .footer-band .main { flex: 1; background: var(--navy); }
</style>
</head>
<body>
  <main class="letterhead">
    <header>
      <div class="brand">
        <div class="brand-name"><span class="brand-dot"></span>VYRLOTEN</div>
        <div class="brand-tagline">Community Health Center</div>
      </div>
      <address class="contact">
        <p class="contact-address">48 Larkfield Crescent,<br>Brantwood, ON K7R 3T5</p>
        <ul class="contact-list">
          <li><svg viewBox="0 0 10 10"><path d="M2 0.5 L3.8 2.6 L2.8 3.8 C3.5 5.3 4.7 6.5 6.2 7.2 L7.4 6.2 L9.5 8 L8.4 9.5 C4.5 9.5 0.5 5.5 0.5 1.6 Z"/></svg>+61 4 5210 3398</li>
          <li><svg viewBox="0 0 10 10"><path d="M0.5 2 H9.5 V8 H0.5 Z M0.5 2 L5 5.5 L9.5 2" stroke="#fff" stroke-width="0.8"/></svg>mail@vyrloten.org</li>
          <li><svg viewBox="0 0 10 10"><circle cx="5" cy="5" r="4.5"/><path d="M0.5 5 H9.5 M5 0.5 C3 3 3 7 5 9.5 M5 0.5 C7 3 7 7 5 9.5" stroke="#fff" stroke-width="0.7" fill="none"/></svg>www.vyrloten.org</li>
        </ul>
      </address>
    </header>

    <section class="letter">
      <p class="salutation">Dear customer,</p>
      <p>Lorem ipsum dolor sit amet, consectetur adipisicing elit, sed do eiusmod tempor incididunt ut labore et dolore magna aliqua. Ut enim ad minim veniam, quis nostrud exercitation ullamco laboris nisi ut aliquip ex ea commodo consequat. Duis aute irure dolor in reprehenderit in voluptate velit esse cillum dolore eu fugiat nulla pariatur. Excepteur sint occaecat cupidatat non proident, sunt in culpa qui officia deserunt mollit anim id est laborum.</p>
      <p>Lorem ipsum dolor sit amet, consectetur adipisicing elit, sed do eiusmod tempor incididunt ut labore et dolore magna aliqua. Ut enim ad minim veniam, quis nostrud exercitation ullamco laboris nisi ut aliquip ex ea commodo consequat. Duis aute irure dolor in reprehenderit in voluptate velit esse cillum dolore eu fugiat nulla pariatur. Excepteur sint occaecat cupidatat non proident, sunt in culpa qui officia deserunt mollit anim id est laborum.</p>
      <p>Lorem ipsum dolor sit amet, consectetur adipisicing elit, sed do eiusmod tempor incididunt ut labore et dolore magna aliqua. Ut enim ad minim veniam, quis nostrud exercitation ullamco laboris nisi ut aliquip ex ea commodo consequat. Duis aute irure dolor in reprehenderit in voluptate velit esse cillum dolore eu fugiat nulla pariatur. Excepteur sint occaecat cupidatat non proident, sunt in culpa qui officia deserunt mollit anim id est laborum.</p>
      <p>Lorem ipsum dolor sit amet, consectetur adipisicing elit, sed do eiusmod tempor incididunt ut labore et dolore magna aliqua. Ut enim ad minim veniam, quis nostrud exercitation ullamco laboris nisi ut aliquip ex ea commodo consequat. Duis aute irure dolor in reprehenderit.</p>
      <p>Yours Sincerely,</p>
      <div class="signature" role="img" aria-label="Handwritten signature"></div>
    </section>

    <footer class="footer-band">
      <span class="accent"></span>
      <span class="main"></span>
    </footer>
  </main>
</body>
</html>
```